The Drifters

Copper Heron Productions is looking for their theatrical poster for their film 'THE DRIFTERS'... It is a zombie appocalypse action film made in NSW Australia. See their facebook page www.pagebook.example/THEDRIFTERSFILM...
Updates
Project Deadline Extended
Reason: i have decided to EXTEND the deadline for 5 more days, as there are some really talented artists reviewing their submissions for us... Thank you to all...
Please review the new uploaded images you may or may not want to use to revierw your submissions
Logo Text
Copper Heron Productions
Look and feel
Each slider illustrates characteristics of the customer's brand and the style your logo design should communicate.

```html
<!DOCTYPE html>
<html lang="en">
<head>
<meta charset="utf-8">
<title>The Drifters – Theatrical Poster</title>
<link href="https://fonts.googleapis.com/css2?family=Bebas+Neue&family=Oswald:wght@400;600&display=swap" rel="stylesheet">
<style>
  :root {
    --blood: #b3121a;
    --blood-deep: #6e070c;
    --blood-dark: #3a0306;
    --bone: #f4efe9;
    --ink: #1a0203;
    --pale: #e9c9c6;
  }
  html, body {
    margin: 0;
    padding: 0;
    width: 800px;
    height: 1200px;
    overflow: hidden;
    background: var(--blood);
  }
  .poster {
    position: relative;
    width: 800px;
    height: 1200px;
    overflow: hidden;
    background: radial-gradient(ellipse at 65% 45%, var(--blood) 0%, var(--blood-deep) 85%, var(--blood-dark) 100%);
    font-family: "Oswald", "Arial Narrow", sans-serif;
    color: var(--bone);
  }
  .hero-photo {
    position: absolute;
    left: 0;
    top: 190px;
    width: 470px;
    height: 830px;
    background:
      radial-gradient(ellipse at 45% 40%, rgba(233,201,198,0.55) 0%, rgba(140,40,40,0.5) 40%, rgba(60,5,8,0) 75%),
      linear-gradient(180deg, rgba(40,4,6,0.0) 0%, rgba(40,4,6,0.45) 60%, rgba(40,4,6,0) 100%);
    border-radius: 0 50% 40% 0 / 0 40% 45% 0;
  }
  .cast {
    position: absolute;
    top: 18px;
    left: 20px;
    right: 20px;
    display: flex;
    justify-content: space-between;
    text-align: center;
  }
  .cast-member {
    width: 180px;
    line-height: 1.15;
  }
  .cast-name {
    display: block;
    font-size: 19px;
    font-weight: 600;
    letter-spacing: 2px;
    text-transform: uppercase;
    color: var(--pale);
  }
  .cast-role {
    display: block;
    font-size: 15px;
    letter-spacing: 1.5px;
    text-transform: uppercase;
    color: var(--bone);
  }
  .title {
    position: absolute;
    inset: 0;
  }
  .title text {
    font-family: "Bebas Neue", "Oswald", sans-serif;
    fill: var(--bone);
  }
  .title .word-the { fill-opacity: 0.92; }
  .tagline {
    position: absolute;
    left: 440px;
    top: 310px;
    font-family: "Bebas Neue", "Oswald", sans-serif;
    font-style: italic;
    font-size: 54px;
    line-height: 0.95;
    letter-spacing: 3px;
    color: var(--bone);
    transform: skewX(-6deg);
  }
  .tagline span { display: block; }
  .tagline .indent-1 { padding-left: 30px; }
  .tagline .indent-2 { padding-left: 60px; }
  .release {
    position: absolute;
    left: 440px;
    right: 24px;
    top: 700px;
    text-align: center;
  }
  .release-date {
    font-family: "Bebas Neue", "Oswald", sans-serif;
    font-size: 40px;
    letter-spacing: 4px;
    line-height: 1;
  }
  .release-date sup { font-size: 20px; }
  .release-page {
    margin-top: 8px;
    font-size: 15px;
    letter-spacing: 2px;
    text-transform: uppercase;
  }
  .billing {
    margin-top: 10px;
    font-family: "Oswald", "Arial Narrow", sans-serif;
    font-size: 9.5px;
    line-height: 1.35;
    letter-spacing: 0.6px;
    text-transform: uppercase;
    color: var(--pale);
    text-align: justify;
  }
  .studio-site {
    margin-top: 16px;
    font-size: 14px;
    letter-spacing: 2px;
    text-transform: uppercase;
  }
  .studio-mark {
    position: absolute;
    right: 24px;
    bottom: 22px;
    display: flex;
    align-items: center;
    gap: 8px;
    font-size: 13px;
    letter-spacing: 1px;
    text-transform: uppercase;
    color: var(--bone);
  }
  .studio-mark .dot {
    width: 22px;
    height: 22px;
    border-radius: 50%;
    background: var(--bone);
  }
</style>
</head>
<body>
<main class="poster">
  <div class="hero-photo" role="img" aria-label="Close-up photograph of a blood-spattered screaming zombie woman"></div>

  <header class="cast">
    <div class="cast-member"><span class="cast-name">Dorian Vale</span><span class="cast-role">'Pierce'</span></div>
    <div class="cast-member"><span class="cast-name">Miles Harrow</span><span class="cast-role">'Eagle Eye'</span></div>
    <div class="cast-member"><span class="cast-name">Tessa Moreau</span><span class="cast-role">'Blaze'</span></div>
    <div class="cast-member"><span class="cast-name">Ivy Calder</span><span class="cast-role">'Faith'</span></div>
  </header>

  <svg class="title" width="800" height="1200" viewBox="0 0 800 1200" aria-label="The Drifters">
    <text class="word-the" x="-20" y="575" font-size="420" textLength="420" lengthAdjust="spacingAndGlyphs">THE</text>
    <text class="word-drift" x="240" y="700" font-size="250" textLength="545" lengthAdjust="spacingAndGlyphs">DRIFT</text>
    <text class="word-ers" x="100" y="1215" font-size="560" textLength="330" lengthAdjust="spacingAndGlyphs">ERS</text>
  </svg>

  <p class="tagline">
    <span>Kill</span>
    <span class="indent-1">or be</span>
    <span class="indent-2">killed...</span>
  </p>

  <section class="release">
    <div class="release-date">Coming December 1<sup>st</sup></div>
    <div class="release-page">pagebook.example/thedriftersfilm</div>
    <p class="billing">Copper Heron Productions presents a film by Alan Reed The Drifters starring Dorian Vale Miles Harrow Tessa Moreau Ivy Calder music by Nora Quinn edited by Sam Pike produced by Lee Marsh written and directed by Alan Reed</p>
    <div class="studio-site">copperheronproductions.example</div>
  </section>

  <div class="studio-mark"><span class="dot"></span><span>Copper Heron</span></div>
</main>
</body>
</html>
```